Harrowgate Estates Business Card for Apartment Buildings

Create business cards for resident managers who run apartment buildings. The audience is the public who are searching for apartment rentals, and current residents who live at the apartment building. Key design element will be incorporating the company logo, however, the logo cannot dominate. The building name and manager name are more important than the logo. Current business card design leaves little room for copy, so we may need to reduce the size on the current card to allow for more space for copy.

Target Market(s)

Adults 18-65 years of age, who are looking for an apartment rental, plus current residents who live at our apartment buildings.

Industry/Entity Type

Property Management

Contact Information for Business Card

A major design element will be use of the company logo. Important property and manager contact information must be part of the design. The size of the logo will need to be reduced to make room for building and manager contact copy.

Font styles to use
Sans Serif

Colors
3176b5
000000
959595
ffffff

Requirements
Must have
• 1) Incorporate the company logo.
• 2) Use the company colors (dark blue, black/grey, over white).
• 3) FEATURE THE BUILDING NAME
• 4) FEATURE THE MANAGER NAME
• 5) The company name is less important than BUILDING and MANAGER
• 6) Manager contact information
• **SEE ATTACHED CREATIVE BRIEF**
Nice to have
• 1) Back of card logo watermark
• 2) Ability to write notes on back of carfd
Should not have
• Avoid letting the company logo dominate the card, the building name and manager are more important than the company logo.

```html
<!DOCTYPE html>
<html lang="en">
<head>
<meta charset="UTF-8">
<title>Harrowgate Estates – Resident Manager Business Card</title>
<link href="https://fonts.googleapis.com/css2?family=Roboto:wght@400;500;700&family=Roboto+Condensed:wght@700&display=swap" rel="stylesheet">
<style>
  :root {
    --brand-blue: #0f6aa6;
    --brand-blue-text: #1d6ea9;
    --ink: #3a3a3a;
    --grey: #959595;
    --card: #f3f3f3;
    --backdrop: #2a2a2a;
    --watermark: #e3e3e3;
  }
  * { margin: 0; padding: 0; box-sizing: border-box; }
  html, body {
    width: 1200px; height: 960px; overflow: hidden;
    background: var(--backdrop);
    font-family: "Roboto", Arial, sans-serif;
  }
  .canvas { position: relative; width: 1200px; height: 960px; }
  .card {
    position: absolute; left: 320px; width: 600px;
    background: var(--card);
    box-shadow: 0 2px 6px rgba(0,0,0,.45);
  }
  .card--front { top: 100px; height: 345px; }
  .card--back { top: 493px; height: 342px; }

  .name-band {
    position: absolute; left: 0; top: 48px;
    width: 372px; height: 68px;
    background: var(--brand-blue);
    padding: 10px 0 0 43px;
    color: #fff;
  }
  .manager-name {
    font-family: "Roboto Condensed", Arial, sans-serif;
    font-weight: 700; font-size: 23px; line-height: 27px;
  }
  .manager-title { font-size: 15px; font-weight: 500; line-height: 19px; }

  .company-name {
    position: absolute; left: 392px; top: 70px;
    font-weight: 700; font-size: 19px; letter-spacing: .5px;
    color: var(--brand-blue-text); text-transform: uppercase;
  }

  .property { position: absolute; left: 38px; top: 220px; }
  .building-name {
    font-weight: 500; font-size: 22px; line-height: 26px;
    color: var(--brand-blue-text);
  }
  .address { font-size: 14px; color: var(--ink); line-height: 18px; }

  .contact-list { margin-top: 10px; font-size: 14px; color: var(--ink); }
  .contact-row { display: flex; align-items: center; height: 19px; }
  .contact-item { display: inline-flex; align-items: center; margin-right: 5px; }
  .contact-item svg { width: 13px; height: 13px; margin-right: 5px; fill: var(--brand-blue); }

  .back-mark {
    position: absolute; inset: 0;
    display: flex; align-items: center; justify-content: center;
    font-weight: 700; font-size: 44px; letter-spacing: 2px;
    color: var(--watermark); text-transform: uppercase;
  }
</style>
</head>
<body>
<div class="canvas">
  <section class="card card--front">
    <div class="name-band">
      <p class="manager-name">Marisol Delgado</p>
      <p class="manager-title">Resident Manager</p>
    </div>
    <p class="company-name">Harrowgate Estates</p>

    <div class="property">
      <h1 class="building-name">Cedar Crest Apartments</h1>
      <p class="address">2847 Larkspur Avenue, Fairview, CA 90210</p>
      <div class="contact-list">
        <div class="contact-row">
          <span class="contact-item">
            <svg viewBox="0 0 16 16" aria-hidden="true"><path d="M3.5 1l2.5 3-1.5 2c1 2 3 4 5 5l2-1.5 3 2.5-1.5 2.5C8 15 1 8 1 2.5z"/></svg>555-210-4830</span>
          <span class="contact-item">
            <svg viewBox="0 0 16 16" aria-hidden="true"><path d="M4 0h8v16H4zM5.5 2v10h5V2z"/></svg>555-374-9162</span>
          <span class="contact-item">
            <svg viewBox="0 0 16 16" aria-hidden="true"><path d="M4 1h8v4H4zM1 6h14v7h-2v-3H3v3H1zM4 11h8v4H4z"/></svg>555-688-0415</span>
        </div>
        <div class="contact-row">
          <span class="contact-item">
            <svg viewBox="0 0 16 16" aria-hidden="true"><path d="M1 4h14v9H1zM1.5 4.5L8 9l6.5-4.5V6L8 10.5 1.5 6z" fill-rule="evenodd"/></svg>marisol@harrowgateest.com</span>
          <span class="contact-item">
            <svg viewBox="0 0 16 16" aria-hidden="true"><circle cx="8" cy="8" r="7"/><path d="M1 8h14M8 1c-3 3-3 11 0 14M8 1c3 3 3 11 0 14" stroke="#f3f3f3" stroke-width="1" fill="none"/></svg>harrowgateest.com</span>
        </div>
      </div>
    </div>
  </section>

  <section class="card card--back">
    <p class="back-mark">Harrowgate Estates</p>
  </section>
</div>
</body>
</html>
```